Animal Eye Clinic needs a Business card

We are a new veterinary ophthalmology practice (Tessaly Animal Eye Care) and we need a business card designed. We only see animal eyes - we are not a regular veterinary clinic. We already have a logo. We are looking for a professional, good looking business card to hand out to our clients. We are looking for something simple but professional and contemporary. Our logo is likely the only picture/graphic that needs to be on the card.
Updates

Contact Information for Business Card

Marisol Dunkley, BSc, DVM, MSc, DipACVO
Veterinary Ophthalmologist

Phone: 250.418.3097
Email: tessalyanimaleyecare@mailbrook.net
Website: tessalyanimaleyecare.net
Address: 1840 Pellworth Rd
Kelowna, BC, V4T 8M3

Colors

Designer to choose colors to be used in the design.

Requirements
Must have
• Our logo (attached)

```html
<!DOCTYPE html>
<html lang="en">
<head>
<meta charset="utf-8">
<title>Tessaly Animal Eye Care – Business Card</title>
<link rel="stylesheet" href="https://fonts.googleapis.com/css2?family=Roboto:wght@300;400;500;700&display=swap">
<style>
  :root {
    --backdrop: #b7a978;
    --card-dark: #141923;
    --card-light: #f1f1f0;
    --teal: #17919f;
    --ink: #111111;
    --muted: #7a7a7a;
    --muted-dark: #8a8f98;
  }
  * { box-sizing: border-box; margin: 0; padding: 0; }
  html, body {
    width: 1200px; height: 960px; overflow: hidden;
    background: var(--backdrop);
    font-family: "Roboto", sans-serif;
  }
  .sheet {
    position: relative; width: 1200px; height: 960px;
    display: flex; align-items: center; justify-content: center; gap: 40px;
  }
  .card {
    position: relative; width: 540px; height: 309px;
    border-radius: 3px; overflow: hidden;
    box-shadow: 0 10px 28px rgba(0,0,0,.22);
  }
  .card--back { background: var(--card-dark); }
  .card--front { background: var(--card-light); }

  .brand {
    display: flex; align-items: center; gap: 10px;
    color: var(--teal); font-weight: 500; white-space: nowrap;
  }
  .brand__dot { border-radius: 50%; background: var(--teal); flex: none; }

  .card--back .brand {
    position: absolute; left: 50%; top: 44%;
    transform: translate(-50%, -50%);
    font-size: 30px;
  }
  .card--back .brand__dot { width: 42px; height: 42px; }
  .card--back .site {
    position: absolute; left: 28px; bottom: 20px;
    font-size: 11px; font-weight: 300; letter-spacing: .5px;
    color: var(--muted-dark);
  }

  .card--front .brand {
    position: absolute; right: 26px; top: 34px; font-size: 17px; gap: 8px;
  }
  .card--front .brand__dot { width: 26px; height: 26px; }

  .person { position: absolute; left: 32px; top: 82px; }
  .person__name { font-size: 28px; font-weight: 500; color: var(--ink); letter-spacing: .3px; }
  .person__creds { font-size: 11px; color: var(--muted); margin-top: 2px; }
  .person__role { font-size: 15px; font-weight: 500; color: var(--teal); margin-top: 1px; }

  .contacts { position: absolute; left: 32px; top: 190px; list-style: none; }
  .contacts li {
    display: flex; align-items: flex-start; gap: 14px;
    font-size: 13px; color: var(--ink); margin-bottom: 8px; line-height: 1.25;
  }
  .contacts svg { width: 16px; height: 16px; flex: none; margin-top: 1px; }
  .contacts .phone { font-size: 16px; font-weight: 500; letter-spacing: .8px; }

  .card--front .site {
    position: absolute; right: 24px; bottom: 22px;
    font-size: 12px; color: var(--teal); letter-spacing: .4px;
  }
</style>
</head>
<body>
<main class="sheet">
  <section class="card card--back" aria-label="Business card back">
    <div class="brand"><span class="brand__dot"></span>Tessaly Animal Eye Care</div>
    <p class="site">www.tessalyanimaleyecare.net</p>
  </section>

  <section class="card card--front" aria-label="Business card front">
    <div class="brand"><span class="brand__dot"></span>Tessaly Animal Eye Care</div>

    <div class="person">
      <h1 class="person__name">Marisol Dunkley</h1>
      <p class="person__creds">BSc, DVM, MSc, DipACVO</p>
      <p class="person__role">Veterinary Ophthalmologist</p>
    </div>

    <ul class="contacts">
      <li>
        <svg viewBox="0 0 24 24" fill="none" stroke="var(--teal)" stroke-width="1.8" stroke-linejoin="round">
          <path d="M5 3h4l2 5-2.5 1.5a11 11 0 0 0 6 6L16 13l5 2v4a2 2 0 0 1-2 2A17 17 0 0 1 3 5a2 2 0 0 1 2-2z"/>
        </svg>
        <span class="phone">250 418 3097</span>
      </li>
      <li>
        <svg viewBox="0 0 24 24" fill="none" stroke="var(--teal)" stroke-width="1.8" stroke-linejoin="round">
          <rect x="3" y="5" width="18" height="14"/><path d="M3 6l9 7 9-7"/>
        </svg>
        <span>tessalyanimaleyecare@mailbrook.net</span>
      </li>
      <li>
        <svg viewBox="0 0 24 24">
          <path fill="var(--teal)" d="M12 2a7 7 0 0 0-7 7c0 5 7 13 7 13s7-8 7-13a7 7 0 0 0-7-7z"/>
          <circle cx="12" cy="9" r="2.6" fill="var(--card-light)"/>
        </svg>
        <span>1840 Pellworth Rd<br>Kelowna, BC, V4T 8M3</span>
      </li>
    </ul>

    <p class="site">www.tessalyanimaleyecare.net</p>
  </section>
</main>
</body>
</html>
```